Plastic Surgery Landing Page

We are a husband and wife team who own a plastic surgery practice in California. The plastic surgeon is Dr. Martin Kessingale. His wife, Tessa is his nurse practitioner.

Our plastic surgery practice is looking for a designer to create landing pages for various procedures that we offer. We will be starting with one procedure, but if we like the work, we will be creating many more. Our first page will promote a surgery called a Brazilian Butt Lift. Our hope is that the page will educate patients briefly on the procedure, but more than anything, get them to give us their contact information so that our Nurse Practitioner, Tessa can connect with them on a more personal level.

Maintaining the high quality of our brand is important. I have attached several documents that specifically lay out colors, fonts, and overall appearance. We also encourage you to visit our website: www.brightwaveplasticsurgery.example to get an idea of what we like aesthetically.

With regards to images or stock photos, we do not like nudity or anything that is overtly sexy or might be considered offensive. Our patients are real women who want to look sexy, but not necessarily like porn stars. Looking forward to seeing what you come up with!

Industry/Entity Type

Plastic

```html
<!DOCTYPE html>
<html lang="en">
<head>
<meta charset="utf-8">
<title>Brightwave Plastic Surgery – Landing Page</title>
<link rel="stylesheet" href="https://fonts.googleapis.com/css2?family=Open+Sans:wght@300;400;600&family=Oswald:wght@500&family=Tinos:ital@0;1&display=swap">
<style>
  :root {
    --header-grey: #e0e0de;
    --page-dark: #231f20;
    --divider-white: #ffffff;
    --brand-navy: #454a6b;
    --panel-blue: #2c5e94;
    --field-white: #ffffff;
    --label-ink: #2b2b2b;
    --signup-cyan: #0ea4e0;
    --button-sand: #c4b59b;
    --photo-sky: #c9d3d8;
    --photo-hills: #6f7a62;
    --photo-field: #b7a583;
  }
  * { box-sizing: border-box; margin: 0; padding: 0; }
  html, body { width: 1200px; height: 822px; overflow: hidden; }
  body {
    position: relative;
    background: var(--page-dark);
    font-family: "Open Sans", Arial, sans-serif;
  }

  /* Header */
  .site-header {
    position: absolute; left: 0; top: 0;
    width: 1200px; height: 200px;
    background: var(--header-grey);
    border-bottom: 9px solid var(--divider-white);
    height: 209px;
  }
  .brand { position: absolute; left: 33px; top: 40px; width: 280px; text-align: center; color: var(--brand-navy); }
  .brand-mark { display: block; margin: 0 auto 8px; }
  .brand-name { font-size: 34px; font-weight: 400; letter-spacing: 7px; line-height: 1; }
  .brand-sub { font-size: 15px; font-weight: 400; letter-spacing: 1px; margin-top: 10px; }

  /* Hero photo area */
  .hero-photo {
    position: absolute; left: 12px; top: 211px;
    width: 416px; height: 589px;
    background: linear-gradient(180deg, var(--photo-sky) 0%, var(--photo-hills) 28%, var(--photo-field) 48%, #8d7f6a 100%);
  }

  /* Quote panel */
  .quote-panel {
    position: absolute; left: 440px; top: 226px;
    width: 389px; height: 429px;
    background: var(--panel-blue);
    color: #fff;
    font-family: "Tinos", "Times New Roman", serif;
    font-style: italic;
    font-size: 37px;
  }
  .quote-line { position: absolute; white-space: nowrap; line-height: 1; }

  /* Newsletter */
  .newsletter { position: absolute; left: 473px; top: 688px; }
  .newsletter-title {
    font-family: "Oswald", "Arial Narrow", sans-serif;
    font-weight: 500; font-size: 22px; color: #fff; letter-spacing: 0.3px;
    margin-left: 3px; line-height: 1;
  }
  .newsletter-form { position: absolute; top: 49px; left: 0; width: 330px; }
  .newsletter-input {
    position: absolute; left: 0; top: 0; width: 204px; height: 32px;
    background: var(--field-white); border: 1px solid #999; border-radius: 7px;
    font-family: "Tinos", "Times New Roman", serif; font-size: 16px; color: #111;
    padding: 6px 9px; line-height: 1;
  }
  .newsletter-button {
    position: absolute; left: 229px; top: 0; width: 93px; height: 32px;
    background: var(--signup-cyan); border-radius: 7px;
    font-family: "Tinos", "Times New Roman", serif; font-size: 18px; color: #fff;
    text-align: center; line-height: 32px;
  }

  /* Contact panel */
  .contact-panel {
    position: absolute; left: 842px; top: 227px;
    width: 336px; height: 572px;
    background: var(--panel-blue);
  }
  .contact-title {
    position: absolute; left: 22px; top: 30px;
    font-size: 50px; font-weight: 300; color: #fff; line-height: 1; letter-spacing: 0.5px;
  }
  .field {
    position: absolute; background: var(--field-white); border-radius: 7px;
    font-size: 11px; color: var(--label-ink); text-transform: uppercase;
    padding: 20px 0 0 10px; line-height: 1; letter-spacing: 0.3px;
  }
  .field.tall { padding-top: 25px; }
  .send-button {
    position: absolute; left: 20px; top: 502px; width: 288px; height: 60px;
    background: var(--button-sand); border-radius: 8px;
    font-size: 19px; color: var(--label-ink); text-align: center; line-height: 60px;
  }
</style>
</head>
<body>

<header class="site-header">
  <div class="brand">
    <svg class="brand-mark" width="44" height="44" viewBox="0 0 44 44" aria-hidden="true">
      <circle cx="22" cy="22" r="22" fill="var(--brand-navy)"/>
    </svg>
    <div class="brand-name">BRIGHTWAVE</div>
    <div class="brand-sub">Plastic Surgery</div>
  </div>
</header>

<div class="hero-photo" role="img" aria-label="Photo of the surgeon and his wife standing together outdoors in a sunlit field with hills behind"></div>

<section class="quote-panel">
  <span class="quote-line" style="left:98px; top:82px;">Love yourself,</span>
  <span class="quote-line" style="left:98px; top:130px;">Be yourself,</span>
  <span class="quote-line" style="left:175px; top:197px;">&amp;</span>
  <span class="quote-line" style="left:41px; top:257px;">Shine brighter than</span>
  <span class="quote-line" style="left:103px; top:312px;">Ever before.</span>
</section>

<section class="newsletter">
  <h2 class="newsletter-title">NEWSLETTER SIGNUP</h2>
  <div class="newsletter-form">
    <div class="newsletter-input">Email address</div>
    <div class="newsletter-button">SIGNUP</div>
  </div>
</section>

<section class="contact-panel">
  <h2 class="contact-title">CONTACT US</h2>
  <div class="field" style="left:20px; top:112px; width:142px; height:52px;">First name</div>
  <div class="field" style="left:166px; top:112px; width:142px; height:52px;">Last name</div>
  <div class="field tall" style="left:20px; top:167px; width:142px; height:52px;">Age</div>
  <div class="field" style="left:166px; top:167px; width:142px; height:52px;">Gender</div>
  <div class="field" style="left:20px; top:224px; width:288px; height:54px;">Email</div>
  <div class="field tall" style="left:20px; top:284px; width:288px; height:54px;">Phone</div>
  <div class="field" style="left:20px; top:343px; width:288px; height:149px;">Message</div>
  <div class="send-button">SEND A MESSAGE</div>
</section>

</body>
</html>
```